Flyer-Design für IT-Systemhaus
Zielgruppe
Wir sind ein IT Systemhaus mit einem Scherpunkt auf Wireless LAN für Gewerbekunden
https://www.kovalmar-beispiel.de/wlan-beratung/
Aufgabenstellung
Im Anhang finden Sie einige Stichpunkte/Texte und eine PPT mit Grafiken, sowie unser Briefpapier.
Ziel ist es 1 Flyer A4 Einseitig zu erhalten – Wir benötigen diesen As soon as possible
Das Thema lautet hier:
1. WLAN für Bauunternehmen / Elektriker
Grafiken können Sie aus der PPT oder der Webseite entnehmen
Die Flyer sollten im oberen Bereich wie unser Briefpapier aussehen und Farbmäßig unserem CD entsprechen
#1e73be
Den Orangeton finde ich leider gerade nicht ☹
An Ergänzenden Grafiken sind wir ebenfalls Interessiert.
Die Welle haben wir leider nicht als Vectorgrafik

```html
<!DOCTYPE html>
<html lang="de">
<head>
<meta charset="utf-8">
<title>Kovalmar Flyer</title>
<link href="https://fonts.googleapis.com/css2?family=Roboto+Condensed:ital,wght@0,400;0,700;1,300;1,400;1,500;1,700&display=swap" rel="stylesheet">
<style>
  :root{
    --brand-blue:#1e73be;
    --mid-blue:#4aa0dc;
    --light-blue:#a9d3f0;
    --pale-blue:#d7ebf8;
    --accent-orange:#ec6a1f;
    --text-grey:#4a4a4a;
    --logo-grey:#555a60;
    --stage-grey:#bfbfbf;
    --paper:#ffffff;
  }
  *{box-sizing:border-box;margin:0;padding:0}
  html,body{width:1200px;height:809px;overflow:hidden}
  body{background:var(--stage-grey);font-family:"Roboto Condensed",Arial,sans-serif;position:relative}
  .divider{position:absolute;left:587px;top:0;width:14px;height:809px;background:#cfcfcf}
  .flyer{position:absolute;top:19px;width:547px;height:773px;background:var(--paper);overflow:hidden;box-shadow:0 1px 3px rgba(0,0,0,.25)}
  .flyer--schools{left:18px}
  .flyer--construction{left:627px}
  .flyer__art{position:absolute;inset:0}
  .brand{position:absolute;right:30px;top:36px;text-align:right}
  .brand__name{font-size:30px;font-weight:400;letter-spacing:2px;color:var(--logo-grey);line-height:1}
  .brand__claim{font-size:16px;font-style:italic;color:var(--brand-blue);margin-top:4px;padding-right:12px}
  .flyer__title{position:absolute;left:24px;font-style:italic;font-weight:500;color:var(--brand-blue);line-height:1}
  .flyer--schools .flyer__title{top:116px;font-size:29px}
  .flyer--construction .flyer__title{top:125px;font-size:29px}
  .block{position:absolute;left:24px;width:330px}
  .block__heading{font-size:13.5px;font-style:italic;font-weight:500;color:var(--text-grey);margin-bottom:6px}
  .bullets{list-style:none}
  .bullets li{position:relative;padding-left:16px;font-size:12px;font-style:italic;font-weight:300;color:var(--text-grey);line-height:18px}
  .bullets li::before{content:"•";position:absolute;left:3px;top:0;font-size:10px}
  .service{position:absolute;width:120px;text-align:center}
  .service__icon{width:52px;height:52px;margin:0 auto 6px;border:1.5px solid var(--brand-blue);border-radius:9px;display:flex;align-items:center;justify-content:center}
  .service__label{font-size:13px;font-style:italic;font-weight:500;color:var(--brand-blue);line-height:15px}
  .benefits{position:absolute;left:16px;width:222px;background:var(--brand-blue);color:#fff;padding:14px 14px 0 18px;z-index:1}
  .benefits__heading{font-size:13.5px;font-style:italic;font-weight:500;margin-bottom:8px}
  .benefits ul{list-style:none}
  .benefits li{position:relative;padding-left:10px;font-size:11px;font-style:italic;line-height:13.5px}
  .benefits li::before{content:"•";position:absolute;left:0;font-size:9px}
  .flyer--schools .benefits{top:484px;height:273px}
  .flyer--schools .benefits li{margin-bottom:13px}
  .flyer--construction .benefits{top:561px;height:196px}
  .flyer--construction .benefits li{margin-bottom:11px}
  .photo-circle{position:absolute;width:168px;height:168px;border-radius:50%;border:6px solid var(--accent-orange);z-index:2}
  .flyer--schools .photo-circle{left:206px;top:405px;background:linear-gradient(150deg,#e8e4de,#9aa7b5 55%,#5d6a78)}
  .flyer--construction .photo-circle{left:195px;top:449px;background:linear-gradient(140deg,#e9eef2,#b7c2cc 50%,#7f8a94)}
  .footer-contact{position:absolute;right:12px;bottom:7px;font-size:12px;font-style:italic;font-weight:500;color:#fff;z-index:3}
</style>
</head>
<body>
<div class="divider"></div>

<section class="flyer flyer--schools">
  <svg class="flyer__art" width="547" height="773" viewBox="0 0 547 773">
    <defs>
      <linearGradient id="photoSchool" x1="0" y1="0" x2="1" y2="1">
        <stop offset="0" stop-color="#d9d2c7"/><stop offset=".5" stop-color="#7f95b8"/><stop offset="1" stop-color="#2f4f8a"/>
      </linearGradient>
    </defs>
    <path d="M0 0H547V10C420 14 220 40 0 88Z" fill="var(--pale-blue)"/>
    <path d="M0 0H547V4C400 6 200 24 0 62Z" fill="var(--mid-blue)"/>
    <path d="M0 0H547C380 2 190 10 0 34Z" fill="var(--brand-blue)"/>
    <g role="img" aria-label="Foto: Schüler lernt lachend am Tablet im Klassenzimmer">
      <path d="M240 512L547 460V773H240Z" fill="url(#photoSchool)"/>
    </g>
    <path d="M0 728C180 690 380 700 547 690V773H0Z" fill="var(--light-blue)"/>
    <path d="M0 748C200 722 380 728 547 724V773H0Z" fill="var(--brand-blue)"/>
  </svg>

  <div class="brand"><div class="brand__name">KOVALMAR</div><div class="brand__claim">WLAN mit System</div></div>
  <h1 class="flyer__title">DigitalPakt Schulen</h1>

  <div class="block" style="top:161px">
    <h2 class="block__heading">Mehrwert für die Schule:</h2>
    <ul class="bullets">
      <li>90% der Kosten werden vom Staat übernommen</li>
      <li>Reputationsvorteil durch digitales Lernangebot</li>
      <li>Moderne Unterrichtsmethoden</li>
    </ul>
  </div>
  <div class="block" style="top:266px">
    <h2 class="block__heading">Mehrwert für die Schüler:</h2>
    <ul class="bullets">
      <li>Routinierter Umgang mit modernen Medien</li>
      <li>Verbesserte Lernerfolge</li>
      <li>Zeitgemäße Medienkompetenzen</li>
    </ul>
  </div>
  <div class="block" style="top:370px">
    <h2 class="block__heading">Die Kovalmar GmbH bietet:</h2>
    <ul class="bullets">
      <li>Unterstützung während der Antragsstellung</li>
      <li>Erfahrung mit Schulen</li>
      <li style="line-height:15px">Professionelle WLAN-Beratung<br>von Konzept bis zur Konfiguration</li>
    </ul>
  </div>

  <div class="service" style="left:362px;top:145px">
    <div class="service__icon"><svg width="34" height="30" viewBox="0 0 34 30"><g fill="none" stroke="var(--accent-orange)" stroke-width="3.5" stroke-linecap="round"><path d="M3 11C11 3 23 3 31 11"/><path d="M8 16C13 11 21 11 26 16"/><path d="M13 21C15 19 19 19 21 21"/></g><circle cx="17" cy="26" r="2.6" fill="var(--accent-orange)"/></svg></div>
    <div class="service__label">WLAN Lösungen</div>
  </div>
  <div class="service" style="left:362px;top:240px">
    <div class="service__icon"><svg width="36" height="34" viewBox="0 0 36 34"><rect x="2" y="3" width="30" height="21" rx="2" fill="var(--accent-orange)"/><rect x="5" y="6" width="24" height="15" fill="#fff" opacity=".25"/><rect x="13" y="24" width="8" height="5" fill="var(--accent-orange)"/><rect x="9" y="29" width="16" height="2.5" fill="var(--accent-orange)"/><rect x="24" y="21" width="10" height="8" rx="1" fill="var(--brand-blue)"/><path d="M26 21v-2.5a3 3 0 0 1 6 0V21" fill="none" stroke="var(--brand-blue)" stroke-width="1.6"/></svg></div>
    <div class="service__label">IT Sicherheit</div>
  </div>
  <div class="service" style="left:362px;top:337px">
    <div class="service__icon"><svg width="36" height="34" viewBox="0 0 36 34"><path d="M6 18V15a12 12 0 0 1 24 0v3" fill="none" stroke="var(--accent-orange)" stroke-width="3"/><rect x="3" y="15" width="6" height="10" rx="2" fill="var(--accent-orange)"/><rect x="27" y="15" width="6" height="10" rx="2" fill="var(--accent-orange)"/><path d="M30 25c0 4-4 6-9 6" fill="none" stroke="var(--accent-orange)" stroke-width="2"/><circle cx="28" cy="28" r="5" fill="var(--brand-blue)"/><text x="28" y="30.5" font-size="7" fill="#fff" text-anchor="middle" font-family="Roboto Condensed, sans-serif">?</text></svg></div>
    <div class="service__label">Support vom<br>Fachmann</div>
  </div>

  <div class="photo-circle" role="img" aria-label="Foto: Schülerin arbeitet am Laptop im Klassenraum"></div>

  <div class="benefits">
    <h2 class="benefits__heading">Ihre Vorteile auf einen Blick:</h2>
    <ul>
      <li>Integration von modernen<br>Lernmethoden</li>
      <li>Ständig verfügbare, digitale<br>Lernumgebungen</li>
      <li>Digitale Kommunikationswege<br>zwischen Lehrern und Schülern</li>
      <li>Direktes Feedback für Schüler<br>und Lehrer</li>
      <li>Einbindung von BYOD-Konzepten<br>und Screencasting</li>
      <li>Remote-Zugriff auf den Unterricht<br>von Zuhause</li>
    </ul>
  </div>

  <div class="footer-contact">info@kovalmar-beispiel.de | www.kovalmar-beispiel.de</div>
</section>

<section class="flyer flyer--construction">
  <svg class="flyer__art" width="547" height="773" viewBox="0 0 547 773">
    <defs>
      <linearGradient id="photoBuild" x1="0" y1="0" x2="1" y2="1">
        <stop offset="0" stop-color="#eef0f2"/><stop offset=".5" stop-color="#d8d4ce"/><stop offset="1" stop-color="#b9b3aa"/>
      </linearGradient>
    </defs>
    <path d="M0 0H547V10C420 14 220 40 0 88Z" fill="var(--pale-blue)"/>
    <path d="M0 0H547V4C400 6 200 24 0 62Z" fill="var(--mid-blue)"/>
    <path d="M0 0H547C380 2 190 10 0 34Z" fill="var(--brand-blue)"/>
    <g role="img" aria-label="Foto: Hände über Bauplänen und Laptop auf dem Schreibtisch">
      <path d="M150 560C300 520 420 480 547 440V773H150Z" fill="url(#photoBuild)"/>
    </g>
    <path d="M0 728C180 690 380 700 547 690V773H0Z" fill="var(--light-blue)"/>
    <path d="M0 748C200 722 380 728 547 724V773H0Z" fill="var(--brand-blue)"/>
  </svg>

  <div class="brand"><div class="brand__name">KOVALMAR</div><div class="brand__claim">WLAN mit System</div></div>
  <h1 class="flyer__title">WLAN für Bauunternehmen &amp; Elektriker</h1>

  <div class="block" style="top:162px">
    <h2 class="block__heading">Mehrwerte für Ihr Unternehmen:</h2>
    <ul class="bullets">
      <li>Alleinstellungsmarkmal gegenüber Mitbewerbern</li>
      <li>Schaffung neuer (monetärer) Mehrwerte</li>
      <li>Risikominderung für WLAN Fehlplanungen</li>
    </ul>
  </div>
  <div class="block" style="top:254px">
    <h2 class="block__heading">Mehrwerte für Ihre Kunden:</h2>
    <ul class="bullets">
      <li>Professionelles WLAN bereits beim Einzug</li>
      <li>WLAN nach Stand der Technik</li>
      <li>Investitionskosten für WLAN bereits im<br>Rahmen der Gebäudefinanzierung planbar</li>
      <li>Investitionskosten über Gebäudefinanzierung<br>planbar</li>
    </ul>
  </div>
  <div class="block" style="top:399px">
    <h2 class="block__heading">Die Kovalmar GmbH bietet:</h2>
    <ul class="bullets">
      <li>Erfahrung mit Bauvorhaben in privaten<br>und öffentlichen Bereichen</li>
      <li>ISO 9001 und ISO 27001 zertifiziert</li>
      <li>Professionelle WLAN-Beratung<br>von Konzept bis zur<br>Konfiguration</li>
    </ul>
  </div>

  <div class="service" style="left:361px;top:163px">
    <div class="service__icon"><svg width="36" height="34" viewBox="0 0 36 34"><rect x="4" y="5" width="24" height="22" fill="none" stroke="var(--accent-orange)" stroke-width="2.5"/><path d="M9 10h14v12H9zM16 10v6h7" fill="none" stroke="var(--accent-orange)" stroke-width="1.8"/><g fill="none" stroke="var(--brand-blue)" stroke-width="1.8" stroke-linecap="round"><path d="M24 25a7 7 0 0 1 10 0"/><path d="M26.5 28a3.5 3.5 0 0 1 5 0"/></g><circle cx="29" cy="31" r="1.4" fill="var(--brand-blue)"/></svg></div>
    <div class="service__label">WLAN Planung</div>
  </div>
  <div class="service" style="left:361px;top:254px">
    <div class="service__icon"><svg width="36" height="34" viewBox="0 0 36 34"><path d="M4 16L18 4L32 16M8 13V30H28V13" fill="none" stroke="var(--accent-orange)" stroke-width="2.6" stroke-linejoin="round"/><circle cx="18" cy="19" r="2" fill="var(--accent-orange)"/><g fill="none" stroke="var(--accent-orange)" stroke-width="1.6"><path d="M14 16a5 5 0 0 0 0 6M22 16a5 5 0 0 1 0 6"/></g><g fill="none" stroke="var(--brand-blue)" stroke-width="1.8" stroke-linecap="round"><path d="M23 27a7 7 0 0 1 10 0"/><path d="M25.5 30a3.5 3.5 0 0 1 5 0"/></g></svg></div>
    <div class="service__label">WLAN<br>Ausleuchtung</div>
  </div>
  <div class="service" style="left:361px;top:356px">
    <div class="service__icon"><svg width="36" height="34" viewBox="0 0 36 34"><rect x="5" y="4" width="16" height="27" fill="var(--accent-orange)"/><rect x="21" y="14" width="8" height="17" fill="var(--accent-orange)"/><g fill="#fff"><rect x="8" y="8" width="3" height="3"/><rect x="14" y="8" width="3" height="3"/><rect x="8" y="14" width="3" height="3"/><rect x="14" y="14" width="3" height="3"/><rect x="8" y="20" width="3" height="3"/><rect x="14" y="20" width="3" height="3"/></g><g fill="none" stroke="var(--brand-blue)" stroke-width="1.8" stroke-linecap="round"><path d="M24 25a7 7 0 0 1 10 0"/><path d="M26.5 28a3.5 3.5 0 0 1 5 0"/></g><circle cx="29" cy="31" r="1.4" fill="var(--brand-blue)"/></svg></div>
    <div class="service__label">WLAN<br>Infrastruktur</div>
  </div>

  <div class="photo-circle" role="img" aria-label="Foto: Hände tippen auf einer Laptop-Tastatur"></div>

  <div class="benefits">
    <h2 class="benefits__heading">Ihre Vorteile auf einen Blick:</h2>
    <ul>
      <li>Planung und Ausleuchtung vom Profi</li>
      <li>Konfiguration und Montage durch<br>zertifizierte Techniker</li>
      <li>Kompetente und objektive Beratung<br>vom Fachmann</li>
      <li>Maximale Effizienz und<br>kalkulierbare Kosten</li>
    </ul>
  </div>

  <div class="footer-contact">info@kovalmar-beispiel.de | www.kovalmar-beispiel.de</div>
</section>
</body>
</html>
```